Design profile for MuroDeck Nordhaven

I had a logo competition here recently, and was left with two logos that I could not choose between. Therefore, I create this competition where I want a complete design package or a visual identity for the company. I want you to create design elements that can be used both in print and online. (letterhead, envelopes, business card, website, facebook, etc.) I have also attached a picture of the car I have ordered. I'm happy if you can show how the design can be used on that as well.
What is important is that the logos are treated individually, and that the design you create reflects or builds up under the logo. I want the design to be recognizable and to have a connection with the logo and what we do. (take fizzo lumo as an example. if you remove the name, but keep the red color and the white line, then you will recognize which brand it is about right away)
You choose whether you want to make proposals only for one logo, or or both, but it is important that they are treated individually. The best overall package determines which logo I use.
I have also added an image that you can use as an example background if you want it in a facebook banner for example.
It is important that the design looks professional and unique. A number of designs have come in, but many of the designs are very similar and general. Here is a video of the printer if you need inspiration: https://clipvault.example/v/Q8ZtrMx2LwK

Industry/Entity Type

WallPrinting

Requirements
Must have
• Unique an professional design that can be used both online and print
Nice to have
• Show how to use the design on a VX Tully. (see photos attached)
Should not have
• The design can be simple, but not too simple and general. I want it to give the company an identity

```html
<!DOCTYPE html>
<html lang="en">
<head>
<meta charset="utf-8">
<title>MuroDeck Nordhaven – Business Card</title>
<link rel="stylesheet" href="https://fonts.googleapis.com/css2?family=Quicksand:wght@500;600;700&display=swap">
<style>
  :root {
    --page-bg: #e6e1db;
    --frost-top: #f3f1ee;
    --frost-mid: #e9e6e3;
    --frost-low: #ead9dc;
    --ink-dark: #1d1d1f;
    --card-black: #0b0b0c;
    --card-black-soft: #1a1a1c;
    --divider-band: #1c2433;
    --divider-gray: #8c8378;
    --name-warm: #cdbb9c;
    --name-light: #dcdcdc;
    --role-blue: #1f6d9c;
    --detail-text: #d9d0c2;
    --icon-blue: #1f6d9c;
  }
  * { box-sizing: border-box; margin: 0; padding: 0; }
  html, body {
    width: 1200px; height: 969px; overflow: hidden;
    background: var(--page-bg);
    font-family: "Quicksand", sans-serif;
  }
  .business-card {
    position: absolute; left: 100px; top: 200px;
    width: 1000px; height: 569px;
    border-radius: 28px; overflow: hidden;
    display: flex;
    box-shadow: 0 18px 40px rgba(0,0,0,.18);
  }
  .card-front {
    width: 522px; height: 100%;
    background: linear-gradient(180deg, var(--frost-top) 0%, var(--frost-mid) 55%, var(--frost-low) 85%, var(--frost-mid) 100%);
    position: relative;
  }
  .brand-name {
    position: absolute; left: 0; right: 0; top: 262px;
    text-align: center; color: var(--ink-dark); font-weight: 700;
  }
  .brand-name .brand-main { display: block; font-size: 62px; line-height: 1; letter-spacing: -1px; }
  .brand-name .brand-sub { display: block; font-size: 19px; letter-spacing: 13px; margin-top: 16px; padding-left: 13px; }
  .card-divider {
    width: 18px; height: 100%; flex: none;
    background: var(--divider-band);
    border-right: 6px solid var(--divider-gray);
  }
  .card-back {
    flex: 1; height: 100%;
    background: radial-gradient(ellipse at 35% 40%, var(--card-black-soft) 0%, var(--card-black) 70%);
    padding: 120px 0 0 65px;
    color: var(--detail-text);
  }
  .person-name { font-size: 34px; font-weight: 700; line-height: 1.1; color: var(--name-light); }
  .person-name .first { color: var(--name-warm); }
  .person-role { font-size: 20px; font-weight: 500; color: var(--role-blue); letter-spacing: .5px; margin-top: 2px; }
  .address { font-size: 20px; font-weight: 500; line-height: 28px; margin-top: 14px; letter-spacing: .4px; }
  .contact-list { list-style: none; margin-top: 14px; }
  .contact-list li {
    display: flex; align-items: center; gap: 12px;
    font-size: 20px; font-weight: 500; line-height: 28px; letter-spacing: .4px;
  }
  .contact-list svg { width: 18px; height: 18px; flex: none; }
</style>
</head>
<body>
  <div class="business-card">
    <section class="card-front">
      <div class="brand-name">
        <span class="brand-main">MuroDeck</span>
        <span class="brand-sub">NORDHAVEN</span>
      </div>
    </section>

    <div class="card-divider" aria-hidden="true"></div>

    <section class="card-back">
      <h1 class="person-name"><span class="first">Henrik</span> Vale</h1>
      <p class="person-role">President</p>
      <p class="address">4120 Larchmere Row<br>Brookhaven, Ostland 20918</p>
      <ul class="contact-list">
        <li>
          <svg viewBox="0 0 24 24" aria-hidden="true"><path fill="var(--icon-blue)" d="M6.6 10.8a15 15 0 0 0 6.6 6.6l2.2-2.2c.3-.3.7-.4 1-.2 1.1.4 2.3.6 3.6.6.6 0 1 .4 1 1V20c0 .6-.4 1-1 1A17 17 0 0 1 3 4c0-.6.4-1 1-1h3.5c.6 0 1 .4 1 1 0 1.3.2 2.5.6 3.6.1.3 0 .7-.2 1z"/></svg>
          555-208-1473
        </li>
        <li>
          <svg viewBox="0 0 24 24" aria-hidden="true"><rect x="6" y="2" width="12" height="20" rx="2" fill="none" stroke="var(--icon-blue)" stroke-width="2"/><circle cx="12" cy="18" r="1.2" fill="var(--icon-blue)"/></svg>
          555-391-6620
        </li>
        <li>
          <svg viewBox="0 0 24 24" aria-hidden="true"><rect x="6" y="2" width="12" height="6" fill="var(--icon-blue)"/><rect x="2" y="9" width="20" height="9" rx="2" fill="var(--icon-blue)"/><rect x="6" y="15" width="12" height="7" fill="#9cc4dc"/></svg>
          555-744-0259
        </li>
        <li>
          <svg viewBox="0 0 24 24" aria-hidden="true"><rect x="2" y="5" width="20" height="14" rx="1.5" fill="var(--icon-blue)"/><path d="M3 6l9 7 9-7" fill="none" stroke="#0b0b0c" stroke-width="1.6"/></svg>
          vale@murodeck.example
        </li>
        <li>
          <svg viewBox="0 0 24 24" aria-hidden="true"><circle cx="12" cy="12" r="9.5" fill="none" stroke="var(--icon-blue)" stroke-width="2"/><ellipse cx="12" cy="12" rx="4" ry="9.5" fill="none" stroke="var(--icon-blue)" stroke-width="1.6"/><path d="M2.5 12h19" stroke="var(--icon-blue)" stroke-width="1.6"/></svg>
          www.murodeck.example
        </li>
      </ul>
    </section>
  </div>
</body>
</html>
```